こんにちは、

森川建設の森川です!

弊社は、
八王子市で足場屋を営んでおります!

筋トレ大好きな若者向けの求人用のチラシを作ってもらいたいです。

アルバイト募集って感じで、

・ロングタイム
8:00〜17:00で1日16,000円

・ショートタイム
10:00〜16:00で1日13,000円

置き場などでの残業はありません。

筋肉、体幹を、鍛えて、
かつ、

ワンチャン技術も身につく!

※筋トレ好きや、格闘家や、アスリートに最適!

-----------------------------
弊社の売り(ここは、入れないほうが良ければ入れなくてもいいです!参考までに)

・会社の理念が、社員満足度を第一にして、会社と、関わる全ての人を潤わす。
・質の高い足場屋さん。技術力も優れている。
・週休2日制
・自分の用事に合わせて好きな日に休める。
・関わる全ての人が 経済的、精神的、時間的に潤うことを目指している。
・チームワークを大事にしている。
・全スタッフ14名
・イベント多数 (毎年海外旅行or国内旅行+レジャー)
・ホームページ morikawakensetsu.info

こんな感じなのですが、これを、イメージしてもらい、見る人に、インパクトと高感度を与えてくれて、口コミや、実際に応募がきたら嬉しいです。

㍿森川建設
A5
片面
シンプル 複雑
単色 カラフル
暗い 明るい
日常 高級
遊び心 厳粛
未来的 伝統的
女性的 男性的
一応会社のイメージカラーは、紺ですが、色は、オススメの色でお願いしたいです!
• 高解像度JPG (.jpg)
• イラストレーター形式 (.ai)
・バス広告のロゴで、バイアスを構築していますので、バス広告のデザインを利用して作っていただけると相乗効果を生むことができるので、お願いしたいです!

あ、このロゴなんか見たことあるのような感じです!
※ですが、上のロゴを入れるのが、あまり良くないと思えば、それは、気にしなくても良いです!1番は、若者を入れたいので、そのためを重視してもらいたいです!

・納品ですが、金額や、条件を少し編集できるようにしたいので、アウトライン化してるものと、されてないものを納品して頂きたいです!
A4でもA6でも使えるようにしたいです!
社内で話し合ったところ、もう少しインパクトの強い印象に残るものができるんじゃ無いかという期待を込めて延長させてもらいました。

・筋肉(鍛えられる)、
・短時間制のアルバイトがある(短時間制の職人系のアルバイトでは、珍しいです。)
・ロングタイムも、選べる。

これが1番伝えたい内容です。

次に、
職人さんは、いまとても減ってきてるので、希少性がかなり高くなっています。先に技術を学んでおくことで、後にブルーオーシャンになるのでは無いか?と予測しています。

これは、僕の伝えたい思い出もありますが、
チラシとして何を目的にしてるかは、
人を入れたいという事が目的なので、

ユーザー側の気持ちになってもらい、

・身体に自信がある人や
・身体にコンプレックスを持っていてムキムキになりたいと考えてる人
・頭を使うよりも身体を動かす事が自分に向いていると感じてる人に

響くような、チラシになることを願っています。

1発で目に引かれて、頭から離れないような、チラシにしてもらいたいです!

よろしくお願いします。

インパクトもあり、なんとなく清潔にも感じて、無駄な主張もなくシンプルで良い作品だと感じました。

多くの素晴らしい作品があり、選定するのにとても困りました。

本当にありがとうございます。

職人の価値向上を目指して、頑張ります!

本当にありがとうございました。

これからも宜しくお願い致します。

```html
<!DOCTYPE html>
<html lang="ja">
<head>
<meta charset="utf-8">
<title>森川建設 アルバイト募集</title>
<link rel="stylesheet" href="https://fonts.googleapis.com/css2?family=Dela+Gothic+One&family=Noto+Sans+JP:wght@500;700;900&display=swap">
<style>
  :root {
    --ink: #23252b;
    --night: #1b1e25;
    --navy: #1d3b73;
    --orange: #f08a1c;
    --cream: #f4ead6;
    --sky: #5cb0ec;
    --white: #ffffff;
  }
  * { margin: 0; padding: 0; box-sizing: border-box; }
  html, body { width: 851px; height: 1200px; overflow: hidden; background: var(--night); }
  .flyer {
    position: relative; width: 851px; height: 1200px; overflow: hidden;
    font-family: "Noto Sans JP", sans-serif; color: var(--cream);
  }
  .hero-art {
    position: absolute; left: 0; top: 0; width: 851px; height: 905px;
    background:
      radial-gradient(ellipse at 58% 45%, #c98a52 0%, rgba(201,138,82,0) 45%),
      linear-gradient(160deg, #3a2a1e 0%, #b8611c 35%, #e8922e 60%, #6e3d18 100%);
  }
  .headline {
    position: absolute; left: 40px; top: 60px; width: 560px; height: 720px;
    font-family: "Noto Sans JP", sans-serif; font-weight: 900; color: var(--ink);
    -webkit-text-stroke: 1.5px var(--cream); paint-order: stroke fill;
  }
  .headline span { position: absolute; line-height: 1; }
  .headline .big { font-size: 132px; }
  .headline .small { font-size: 82px; }
  .headline .last { font-size: 104px; letter-spacing: 2px; }
  .tag {
    position: absolute; left: 452px; top: 30px;
    writing-mode: vertical-rl; font-size: 21px; font-weight: 700; color: var(--white);
    letter-spacing: 3px;
  }
  .call {
    position: absolute; right: 40px; top: 36px;
    writing-mode: vertical-rl; font-family: "Dela Gothic One", sans-serif;
    font-size: 96px; line-height: 1; color: var(--orange); letter-spacing: 2px;
    -webkit-text-stroke: 2px var(--ink); paint-order: stroke fill;
    transform: rotate(6deg);
  }
  .terms { position: absolute; left: 44px; top: 912px; list-style: none; }
  .terms li {
    display: flex; align-items: center; gap: 14px;
    font-size: 30px; font-weight: 700; line-height: 50px; color: var(--cream);
  }
  .terms li::before { content: ""; width: 22px; height: 22px; background: var(--orange); }
  .terms .pay { color: var(--white); }
  .message {
    position: absolute; left: 44px; top: 1024px;
    font-size: 33px; font-weight: 900; line-height: 50px; color: var(--sky);
  }
  .footer {
    position: absolute; left: 0; bottom: 0; width: 851px; height: 72px;
    background: var(--navy); display: flex; align-items: center; padding: 0 40px; gap: 18px;
  }
  .brand-mark { width: 40px; height: 40px; border-radius: 50%; background: var(--white); }
  .brand { display: flex; align-items: center; gap: 6px; color: var(--white); font-weight: 900; }
  .brand .kind { font-size: 13px; writing-mode: vertical-rl; line-height: 1.1; }
  .brand .name { font-size: 34px; letter-spacing: 3px; }
  .address { font-size: 15px; line-height: 22px; color: var(--white); font-weight: 500; margin-left: 10px; font-style: normal; }
</style>
</head>
<body>
<main class="flyer">
  <div class="hero-art" role="img" aria-label="ヘルメットをかぶった筋肉質な足場職人と夜の足場を描いたイラスト"></div>

  <h1 class="headline" aria-label="仲間と身体と足場をつくる。">
    <span class="big" style="left:0;top:0">仲</span>
    <span class="big" style="left:140px;top:-8px">間</span>
    <span class="small" style="left:70px;top:118px">と</span>
    <span class="big" style="left:0;top:190px">身</span>
    <span class="big" style="left:140px;top:175px">体</span>
    <span class="small" style="left:70px;top:305px">と</span>
    <span class="big" style="left:0;top:385px">足</span>
    <span class="big" style="left:140px;top:385px">場</span>
    <span class="small" style="left:282px;top:430px">を</span>
    <span class="last" style="left:250px;top:590px">つくる。</span>
  </h1>
  <p class="tag">君を待っている</p>
  <p class="call">アルバイトしよう!</p>

  <ul class="terms">
    <li>ロングタイム(8:00〜17:00)<span class="pay">1日 16,000円</span></li>
    <li>ショートタイム(10:00〜16:00)<span class="pay">1日 13,000円</span></li>
  </ul>

  <p class="message">身体に自信のある人もない人も、共に鍛え、<br>建設現場の貴重な技術を身に付けよう!!</p>

  <footer class="footer">
    <span class="brand-mark"></span>
    <div class="brand"><span class="kind">株式会社</span><span class="name">森川建設</span></div>
    <address class="address">〒192-0000 東京都八王子市南台町12-5<br>南台ビル1階 TEL:042-000-1234</address>
  </footer>
</main>
</body>
</html>
```